Book Cover for a book on Lantern Road Ventures

I am self-publishing my book on Brindlemark and need a book cover made. Below are the details. See attached templates for size we need to use. I also attached a previous cover we had made that I liked. The problem with it was they were two boys helping each other but the book is about women. I'm open to your ideas on the cover though, but I wanted to show you a style I liked as an idea.
Front of Cover
Book Title: Lantern Road Ventures
Book Subtitle: Loose Pages of a Harbor Keeper
Author Name: Mirela T. Dunbar
Add on the Spine of Cover: Lantern Road Ventures and Mirela T. Dunbar
Back of the Cover Text:
Lantern Road Ventures: Loose Pages of a Harbor Keeper is an honest account of a business owner’s experience attempting to navigate the start-up community while also pursuing spiritual growth. Author Mirela Dunbar defines a spiritual entrepreneur as “someone who runs an enterprise with the purpose of growing love rather than material gain.” This book discusses the three dimensions of Lantern Road Ventures:
1. The business is an integral part of the founder’s spiritual journey.
2. Employees working for the spiritual enterprise, whether they know it or not, encounter this company because it's part of their spiritual path.
3. The business itself has a life force of its own and its purpose is to further the kingdom of heaven on earth.
These three dimensions happen simultaneously and work together to produce the greatest possible result. However, this can feel confusing to a founder juggling these dimensions while also trying to manage and run a business. This is not a formulaic self-help book or roadmap. Rather, it is a compilation of personal reflections that often seem at odds with the traditional world of entrepreneurship.
Below the description add my picture (see attached for my picture)
Bio text:
Mirela Dunbar founded Calveta with the vision of ushering in a life-long education system that shifts away from standardization to one that empowers people to live their purpose. In college, Mirela interned for Open Kettle, a women’s empowerment initiative where she recognized her passion for helping people find their voice. Mirela's 20-year journey has come full circle to empowering other female CEOs who are pursuing the path of Lantern Road Ventures.
NOTE: Please note that Brindlemark puts a bar code on the bottom right of the back cover as is noted on the attached template.
Size template is attached to the brief, here are the sizes typed out:
# Description Width (in) Height (in)
1 Full Cover 12.79 9.25
2 Front Cover 6 9
3 Safe Area 5.875 8.75
4 Bleed 0.125 0.125
5 Margin 0.125 0.125
6 Spine 0.54 9
7 Spine Safe Area 0.415 8.75
8 Spine Margin 0.062 0.062
9 Barcode Margin 0.25 0.25
Pre-publication checklist
BRINDLEMARK TIPS for the final cover:
1. Save as a PDF. Your cover must be a single PDF that includes the back cover, spine, and front cover as one image.
2. Flatten all transparencies. These can cause the file to print with missing or distorted content. Consult your software's documentation to learn how.
3. Embed your fonts. Consult your software's documentation to learn how.
4. Remove crop marks, color bars, template text. Crop marks are lines showing where pages should be trimmed. Color bars are strips with a series of patches used to ensure color balance during printing. Also, remove any template text, PDF creation guides, or software references.
5. Ensure your cover image meets the minimum resolution of 300 DPI (dots per inch).
6. Optimize PDFs. Optimization is useful to reduce your file size, allowing for higher performance when transferring, uploading, viewing, and printing the files.
7. Remove file security. Locked or encrypted files will fail review.
Target Market(s)
Women who want to be CEOs or are currently CEOs of companies.
Industry/Entity Type
Entrepreneurship, business, spirituality
Requirements
Must have
- Just the text on the description. A very welcoming feel.
Nice to have
- I like the idea of having a sunrise/sunset in the image somehow like in the example I attached to the brief, but again I'm open.
Should not have
- Please don't put any yoga or meditation poses or hands outstretched. I have a lot of interesting ones that look like my example so if you are going to submit after Saturday 10/29, please only do so if you have a new idea! Thanks!

```html
<!DOCTYPE html>
<html lang="en">
<head>
<meta charset="utf-8">
<title>Lantern Road Ventures — Book Cover</title>
<link rel="stylesheet" href="https://fonts.googleapis.com/css2?family=Cabin:wght@400&family=Cinzel:wght@400&display=swap">
<style>
  :root {
    --ink: #000000;
    --gold: #f6d300;
    --paper: #ffffff;
    --sun-core: #fff4a8;
    --sun-glow: #d9b64a;
    --sky-haze: #8a7a4a;
    --sky-dusk: #3d3624;
  }
  * { margin: 0; padding: 0; box-sizing: border-box; }
  html, body {
    width: 1200px; height: 897px; overflow: hidden; background: var(--ink);
  }
  .cover {
    position: relative; width: 1200px; height: 897px;
    background: var(--ink); color: var(--paper);
    font-family: "Cabin", "Helvetica Neue", Arial, sans-serif;
  }

  /* Back cover */
  .back-blurb {
    position: absolute; left: 49px; top: 49px; width: 476px;
    font-size: 15.2px; line-height: 20.3px;
  }
  .back-blurb p { text-align: center; }
  .back-blurb .dimensions {
    list-style: none; margin: 20px 0 20px; text-align: left;
  }
  .author-photo {
    position: absolute; left: 23px; top: 605px; width: 106px; height: 106px;
    background: radial-gradient(circle at 50% 45%, #c99a7c 0%, #8a5a3e 38%, #6f8f5a 62%, #4f7442 100%);
  }
  .author-bio {
    position: absolute; left: 146px; top: 605px; width: 380px;
    font-size: 15.2px; line-height: 20.3px; text-align: left;
  }

  /* Spine */
  .spine-title, .spine-author {
    position: absolute; writing-mode: vertical-rl;
    font-family: "Cinzel", "Times New Roman", serif; white-space: nowrap;
  }
  .spine-title { left: 588px; top: 22px; font-size: 23px; color: var(--gold); letter-spacing: 0.5px; }
  .spine-author { left: 587px; top: 643px; font-size: 25px; color: var(--paper); letter-spacing: 1px; }

  /* Front cover */
  .front-scene {
    position: absolute; left: 632px; top: 0; width: 568px; height: 350px;
    background:
      radial-gradient(ellipse 95px 80px at 340px 108px, var(--sun-core) 0%, rgba(240,200,70,0.85) 45%, rgba(217,182,74,0) 100%),
      linear-gradient(180deg, var(--sky-haze) 0%, var(--sun-glow) 30%, var(--sky-dusk) 55%, #0c0a06 80%, var(--ink) 100%);
  }
  .front-type {
    position: absolute; left: 632px; width: 568px; text-align: center;
    font-family: "Cinzel", "Times New Roman", serif; white-space: nowrap;
  }
  .book-title { top: 526px; font-size: 50px; line-height: 54px; color: var(--gold); }
  .book-subtitle { top: 643px; font-size: 27px; color: var(--gold); }
  .book-author { top: 795px; font-size: 50px; color: var(--paper); letter-spacing: 1px; }
</style>
</head>
<body>
<main class="cover">
  <section class="back-blurb">
    <p>Lantern Road Ventures: Loose Pages of a Harbor Keeper is an honest account of a business owner’s experience attempting to navigate the start-up community while also pursuing spiritual growth. Author Mirela Dunbar defines a spiritual entrepreneur as “someone who runs an enterprise with the purpose of growing love rather than material gain.” This book discusses the three dimensions of Lantern Road Ventures:</p>
    <ol class="dimensions">
      <li>1. The business is an integral part of the founder’s spiritual journey.</li>
      <li>2. Employees working for the spiritual enterprise, whether they know it or not, encounter this company because it's part of their spiritual path.</li>
      <li>3. The business itself has a life force of its own and its purpose is to further the kingdom of heaven on earth.</li>
    </ol>
    <p>These three dimensions happen simultaneously and work together to produce the greatest possible result. However, this can feel confusing to a founder juggling these dimensions while also trying to manage and run a business. This is not a formulaic self-help book or roadmap. Rather, it is a compilation of personal reflections that often seem at odds with the traditional world of entrepreneurship.</p>
  </section>

  <div class="author-photo" role="img" aria-label="Author portrait photo"></div>
  <p class="author-bio">Mirela Dunbar founded Calveta with the vision of ushering in a life-long education system that shifts away from standardization to one that empowers people to live their purpose. In college, Mirela interned for Open Kettle, a women’s empowerment initiative where she recognized her passion for helping people find their voice. Mirela's 20-year journey has come full circle to empowering other female CEOs who are pursuing the path of Lantern Road Ventures.</p>

  <div class="spine-title">LANTERN ROAD VENTURES</div>
  <div class="spine-author">MIRELA T. DUNBAR</div>

  <div class="front-scene" role="img" aria-label="Sunset sky over dark hills with silhouetted figures"></div>
  <h1 class="front-type book-title">LANTERN ROAD<br>VENTURES</h1>
  <h2 class="front-type book-subtitle">LOOSE PAGES OF A HARBOR KEEPER</h2>
  <p class="front-type book-author">MIRELA T. DUNBAR</p>
</main>
</body>
</html>
```